IT Company Business Card design

Brisk Loop is a new computer solutions business focusing on setting up servers and computer systems for small to medium sized businesses.

A business client will either request a solution, or support for a current system and we will turn up on site to provide these services.

We are bast in Christchurch, New Zealand.

We are looking for unique business card's that stand out and show off the business in a professional light.

Open to all idea's etc.

Industry/Entity Type

Computer

Requirements
Must have
• Business Logo (AI file attached)
Employee Name
Business title
Business landline number
Cell phone number
Email
Web URL
Nice to have
• Could be nice to have some keywords (possibly on the back) such as:

Business IT solutions
Network installations
Phone solutions
Server management
Software diagnostics

The above is not needed, just an idea.

```html
<!DOCTYPE html>
<html lang="en">
<head>
<meta charset="utf-8">
<title>Brisk Loop – Business Card</title>
<link rel="stylesheet" href="https://fonts.googleapis.com/css2?family=Didact+Gothic&display=swap">
<style>
  :root {
    --page-bg: #d9d6d1;
    --card-paper: #ebebed;
    --navy: #1c2f7e;
    --ink: #2a2a2e;
    --label-blue: #1b4fa3;
    --band-light: #1aa0e0;
    --band-dark: #17409a;
    --back-light: #29a6e6;
    --back-mid: #127cc7;
    --back-dark: #0c3f94;
    --rule: #8d8d92;
  }
  * { margin: 0; padding: 0; box-sizing: border-box; }
  html, body { width: 1200px; height: 900px; overflow: hidden; }
  body {
    background: var(--page-bg);
    font-family: "Didact Gothic", "Century Gothic", sans-serif;
    position: relative;
  }
  .card {
    position: absolute;
    left: 250px;
    width: 700px;
    height: 400px;
    overflow: hidden;
    box-shadow: 0 6px 18px rgba(0,0,0,0.18);
  }
  .card--back {
    top: 35px;
    background: linear-gradient(135deg, var(--back-light) 0%, var(--back-mid) 50%, var(--back-dark) 100%);
  }
  .back-swirl {
    position: absolute;
    left: 170px; top: 10px;
    width: 460px; height: 380px;
    border-radius: 50%;
    background: radial-gradient(circle at 50% 45%, rgba(12,63,148,0.55) 0%, rgba(18,124,199,0.35) 55%, rgba(41,166,230,0) 72%);
  }
  .back-url {
    position: absolute;
    left: 0; right: 0; top: 178px;
    text-align: center;
    color: #ffffff;
    font-size: 22px;
    letter-spacing: 4px;
  }
  .card--front {
    top: 465px;
    background: var(--card-paper);
  }
  .brand {
    position: absolute;
    left: 60px; top: 92px;
    display: flex; align-items: center;
  }
  .brand-dot {
    width: 104px; height: 104px;
    border-radius: 50%;
    background: var(--back-mid);
  }
  .brand-rule {
    width: 2px; height: 78px;
    background: var(--rule);
    margin: 0 22px 0 26px;
  }
  .brand-name {
    font-size: 40px;
    letter-spacing: 5px;
    color: var(--ink);
  }
  .person {
    position: absolute;
    left: 232px; top: 168px;
    color: var(--ink);
  }
  .person-name {
    font-size: 25px;
    color: var(--navy);
    letter-spacing: 0.5px;
  }
  .person-title { font-size: 19px; margin-top: 2px; }
  .contact { margin-top: 10px; font-size: 18px; line-height: 25px; }
  .contact-row { display: flex; }
  .contact-label {
    width: 26px;
    color: var(--label-blue);
    font-weight: bold;
    font-family: Arial, sans-serif;
    font-size: 15px;
  }
  .address { margin-top: 6px; font-size: 18px; }
  .front-band { position: absolute; left: 0; bottom: 0; width: 700px; height: 60px; }
</style>
</head>
<body>
  <section class="card card--back" aria-label="Card back">
    <div class="back-swirl" role="img" aria-label="Soft blue circular swirl decoration"></div>
    <p class="back-url">www.briskloop.com</p>
  </section>

  <section class="card card--front" aria-label="Card front">
    <div class="brand">
      <div class="brand-dot"></div>
      <div class="brand-rule"></div>
      <span class="brand-name">BRISK LOOP</span>
    </div>
    <div class="person">
      <p class="person-name">MARA ELLISON</p>
      <p class="person-title">Operation manager</p>
      <div class="contact">
        <div class="contact-row"><span class="contact-label">T</span><span>+64 3 555 0142</span></div>
        <div class="contact-row"><span class="contact-label">F</span><span>+64 21 555 0187</span></div>
        <div class="contact-row"><span class="contact-label"></span><span>name@briskloop.me</span></div>
      </div>
      <p class="address">Harbour Lane - Riverside, PO 375 - City, Country</p>
    </div>
    <svg class="front-band" viewBox="0 0 700 60" aria-hidden="true">
      <polygon points="0,40 700,28 700,60 0,60" fill="var(--band-light)"/>
      <polygon points="260,36 700,20 700,44 420,48" fill="var(--band-dark)"/>
    </svg>
  </section>
</body>
</html>
```